Home page concept, possible logo colour change

There is no need to code a home page, we are just looking for concept ideas.
We have had a logo designed for a new company we are starting named Corvenhall Aluminium Windows & Doors. We are manufacturing bullet resistant window frames. We have had logo designed, we like the concept of the design, but the current colours (black and red) may not be the best option, especially when designing the website home page, and how it interacts with the logo colours. I have also attached the first draft of the home page which we are not happy with. The overall design/navigation is good, we have issues with the darkened out primary image and also the amount of red on the page, it just doesn't feel right. As mentioned before we are happy to look at colour changes to the logo.
Number of Pages Required
1 page
Look and feel
Each slider illustrates characteristics of the customer's brand and the style your logo design should communicate.

```html
<!DOCTYPE html>
<html lang="en">
<head>
<meta charset="utf-8">
<title>Corvenhall Aluminium Windows &amp; Doors</title>
<link href="https://fonts.googleapis.com/css2?family=Poppins:wght@400;500;600;700&display=swap" rel="stylesheet">
<style>
:root{
  --blue:#1e88f0;
  --blue-dark:#1777d9;
  --blue-light:#3b9bf5;
  --ink:#1c1c1c;
  --text:#333;
  --muted:#555;
  --grey-bg:#f1f1f1;
  --white:#fff;
  --line:#dfe6ee;
}
*{margin:0;padding:0;box-sizing:border-box}
html,body{width:1200px;height:3260px;overflow:hidden}
body{font-family:'Poppins',sans-serif;color:var(--text);background:var(--white);position:relative}
.abs{position:absolute}

/* header */
.site-header{position:absolute;top:0;left:0;width:1200px;height:144px;background:var(--white)}
.brand{position:absolute;left:84px;top:40px;display:flex;align-items:center;gap:14px}
.brand-dot{width:44px;height:44px;border-radius:50%;background:var(--blue)}
.brand-name{font-size:22px;font-weight:600;color:var(--blue);line-height:1.15;width:230px}
.main-nav{position:absolute;right:84px;top:44px;display:flex;align-items:center;gap:58px;font-size:17px;color:var(--ink)}
.btn-enquiry{background:var(--blue);color:var(--white);padding:16px 26px;border-radius:4px;font-size:17px}

/* hero */
.hero{position:absolute;top:144px;left:0;width:1200px;height:646px;background:var(--grey-bg)}
.hero-title{position:absolute;left:156px;top:140px;font-size:54px;font-weight:700;color:var(--blue);line-height:64px;letter-spacing:.5px}
.hero-sub{position:absolute;left:156px;top:286px;font-size:32px;font-weight:500;color:var(--ink)}
.hero-copy{position:absolute;left:156px;top:350px;width:470px;font-size:17px;line-height:26px;color:var(--muted)}
.pill-btn{position:absolute;display:flex;align-items:center;gap:18px;background:var(--blue);color:var(--white);font-size:17px;font-weight:500;border-radius:34px;padding:0 10px 0 32px;height:68px}
.pill-btn .arrow-circle{width:46px;height:46px;border-radius:50%;background:var(--white);display:flex;align-items:center;justify-content:center}
.hero-door{position:absolute;left:790px;top:56px;width:120px;height:560px;background:linear-gradient(90deg,#8d9aa6,#c9d2da 30%,#aeb9c3 70%,#7f8c98);border-radius:3px}

/* features */
.features{position:absolute;top:790px;left:0;width:1200px;height:410px;background:var(--white)}
.feature{position:absolute;top:70px;width:320px;text-align:center}
.feature-icon{width:164px;height:164px;border-radius:50%;border:3px solid var(--line);margin:0 auto;display:flex;align-items:center;justify-content:center}
.feature-icon span{width:138px;height:138px;border-radius:50%;background:var(--blue);display:flex;align-items:center;justify-content:center}
.feature h3{margin-top:24px;font-size:22px;font-weight:500;color:var(--blue)}
.feature p{margin-top:8px;font-size:16px;line-height:25px;color:var(--muted)}

/* products */
.products{position:absolute;top:1200px;left:0;width:1200px;height:980px;background:var(--grey-bg)}
.section-title{position:absolute;left:0;top:56px;width:1200px;text-align:center;font-size:42px;font-weight:600;color:var(--blue)}
.product-card{position:absolute;top:185px;width:320px;height:545px;background:var(--white)}
.product-image{height:305px}
.product-card h3{text-align:center;margin-top:28px;font-size:26px;font-weight:500;color:var(--blue)}
.product-card p{margin:16px 28px 0;font-size:16px;line-height:23px;color:var(--muted);text-align:justify}
.card-arrow{position:absolute;left:136px;bottom:-24px;width:48px;height:48px;border-radius:50%;background:var(--blue);display:flex;align-items:center;justify-content:center}

/* process */
.process{position:absolute;top:2180px;left:0;width:1200px;height:740px;background:var(--white)}
.step{position:absolute;left:92px;width:540px;height:110px;border-bottom:2px solid var(--line);display:flex;align-items:center;font-size:20px;font-weight:500;color:var(--ink)}
.step-num{color:var(--blue);width:76px}
.step-toggle{position:absolute;right:0;width:34px;height:34px;border-radius:50%;background:var(--blue);display:flex;align-items:center;justify-content:center}
.step-copy{position:absolute;left:92px;top:440px;width:540px;font-size:16px;line-height:24px;color:var(--muted);text-align:justify}
.process-window{position:absolute;left:780px;top:90px;width:370px;height:430px;background:linear-gradient(135deg,#1b1b1b,#3a3a3a);border-radius:4px;display:flex;align-items:center;justify-content:center}
.process-window span{width:270px;height:320px;background:linear-gradient(135deg,#e7ebee,#c3ccd2)}

/* footer */
.site-footer{position:absolute;top:2920px;left:0;width:1200px;height:270px;background:var(--blue)}
.footer-brand{position:absolute;left:84px;top:102px;display:flex;align-items:center;gap:12px}
.footer-brand .brand-dot{background:var(--white);width:40px;height:40px}
.footer-brand .brand-name{color:var(--white);font-size:20px;width:200px}
.footer-col{position:absolute;top:82px;color:var(--white);font-size:16px;line-height:26px}
.footer-col h4{font-size:20px;font-weight:600;margin-bottom:14px}
.contact-line{display:flex;align-items:center;gap:10px}
.badge{width:64px;height:64px;border-radius:50%;background:#2f9b4b;margin:4px 0 0 40px}
.footer-bar{position:absolute;top:3190px;left:0;width:1200px;height:70px;background:var(--blue-light);color:var(--white);font-size:15px}
.footer-bar .copy{position:absolute;left:84px;top:24px}
.footer-bar .links{position:absolute;right:84px;top:24px;display:flex;gap:14px}
</style>
</head>
<body>

<header class="site-header">
  <div class="brand"><span class="brand-dot"></span><span class="brand-name">Corvenhall Aluminium Windows &amp; Doors</span></div>
  <nav class="main-nav">
    <span>Home</span>
    <span>Our Products ▾</span>
    <span>Why Corvenhall</span>
    <span class="btn-enquiry">Make an Enquiry</span>
  </nav>
</header>

<section class="hero">
  <h1 class="hero-title">BULLET RESISTANT<br>WINDOW &amp; DOORS</h1>
  <p class="hero-sub">Your First line of defence</p>
  <p class="hero-copy">Lorem ipsum dolor sit amet, consectetur adipiscing elit, sed do eiusmod tempor incididunt ut labore et dolore magna</p>
  <a class="pill-btn" style="left:156px;top:422px">KNOW MORE <span class="arrow-circle"><svg width="20" height="20" viewBox="0 0 20 20"><path d="M3 10h13M11 5l5 5-5 5" stroke="#1e88f0" stroke-width="2.5" fill="none" stroke-linecap="round"/></svg></span></a>
  <div class="hero-door" role="img" aria-label="Aluminium framed bullet resistant door with frosted glass"></div>
</section>

<section class="features">
  <div class="feature" style="left:140px">
    <div class="feature-icon"><span><svg width="60" height="60" viewBox="0 0 60 60"><path d="M30 6l20 8v14c0 13-9 22-20 26C19 50 10 41 10 28V14z" fill="none" stroke="#fff" stroke-width="4"/><path d="M21 30l7 7 12-13" fill="none" stroke="#fff" stroke-width="4" stroke-linecap="round"/></svg></span></div>
    <h3>Premium Protection</h3>
    <p>Lorem ipsum dolor sit amet, con selghcletur adipiscing elit, sed do</p>
  </div>
  <div class="feature" style="left:440px">
    <div class="feature-icon"><span><svg width="60" height="60" viewBox="0 0 60 60"><path d="M14 46L46 14M14 14l32 32" stroke="#fff" stroke-width="5" stroke-linecap="round"/><circle cx="14" cy="14" r="5" fill="#fff"/><rect x="40" y="40" width="10" height="10" fill="#fff"/></svg></span></div>
    <h3>Aesthetically Designed</h3>
    <p>Lorem ipsum dolor sit amet, con selghcletur adipiscing elit, sed do</p>
  </div>
  <div class="feature" style="left:740px">
    <div class="feature-icon"><span><svg width="64" height="60" viewBox="0 0 64 60"><rect x="6" y="18" width="32" height="22" fill="#fff"/><path d="M38 24h12l8 9v7H38z" fill="#fff"/><circle cx="18" cy="44" r="6" fill="#fff" stroke="#1e88f0" stroke-width="3"/><circle cx="48" cy="44" r="6" fill="#fff" stroke="#1e88f0" stroke-width="3"/></svg></span></div>
    <h3>Promptly Delivered</h3>
    <p>Lorem ipsum dolor sit amet, con selghcletur adipiscing elit, sed do</p>
  </div>
</section>

<section class="products">
  <h2 class="section-title">Superior Protection, Sleek Design</h2>
  <article class="product-card" style="left:76px">
    <div class="product-image" role="img" aria-label="Silver aluminium door with frosted glass" style="background:linear-gradient(90deg,#e9ecef,#c7ced4 50%,#eef0f2)"></div>
    <h3>Product</h3>
    <p>Lorem ipsum dolor sit amet, co nsetg hcletur adipiscing elit, sed do eiusmod tempor inciduy ididunt ut labore et dolore</p>
    <span class="card-arrow"><svg width="20" height="20" viewBox="0 0 20 20"><path d="M3 10h13M11 5l5 5-5 5" stroke="#fff" stroke-width="2.5" fill="none" stroke-linecap="round"/></svg></span>
  </article>
  <article class="product-card" style="left:436px">
    <div class="product-image" role="img" aria-label="Black framed door standing open" style="background:linear-gradient(90deg,#f2f2f2,#9aa3aa 45%,#2b2b2b 55%,#f2f2f2)"></div>
    <h3>Product</h3>
    <p>Lorem ipsum dolor sit amet, co nsetg hcletur adipiscing elit, sed do eiusmod tempor inciduy ididunt ut labore et dolore</p>
    <span class="card-arrow"><svg width="20" height="20" viewBox="0 0 20 20"><path d="M3 10h13M11 5l5 5-5 5" stroke="#fff" stroke-width="2.5" fill="none" stroke-linecap="round"/></svg></span>
  </article>
  <article class="product-card" style="left:796px">
    <div class="product-image" role="img" aria-label="Glass facade with reflective window panels" style="background:linear-gradient(135deg,#4f6a86,#a9c3dc 50%,#2f4661)"></div>
    <h3>Product</h3>
    <p>Lorem ipsum dolor sit amet, co nsetg hcletur adipiscing elit, sed do eiusmod tempor inciduy ididunt ut labore et dolore</p>
    <span class="card-arrow"><svg width="20" height="20" viewBox="0 0 20 20"><path d="M3 10h13M11 5l5 5-5 5" stroke="#fff" stroke-width="2.5" fill="none" stroke-linecap="round"/></svg></span>
  </article>
  <a class="pill-btn" style="left:482px;top:816px;height:72px">ENQUIRE NOW <span class="arrow-circle"><svg width="20" height="20" viewBox="0 0 20 20"><path d="M3 10h13M11 5l5 5-5 5" stroke="#1e88f0" stroke-width="2.5" fill="none" stroke-linecap="round"/></svg></span></a>
</section>

<section class="process">
  <div class="step" style="top:70px"><span class="step-num">01</span>Explore Our Range<span class="step-toggle"><svg width="16" height="16" viewBox="0 0 16 16"><path d="M8 2v12M2 8h12" stroke="#fff" stroke-width="2.5"/></svg></span></div>
  <div class="step" style="top:180px"><span class="step-num">02</span>Make an Enquiry<span class="step-toggle"><svg width="16" height="16" viewBox="0 0 16 16"><path d="M8 2v12M2 8h12" stroke="#fff" stroke-width="2.5"/></svg></span></div>
  <div class="step" style="top:290px;border-bottom:none"><span class="step-num">03</span>Receive Customized Quote<span class="step-toggle"><svg width="16" height="16" viewBox="0 0 16 16"><path d="M2 8h12" stroke="#fff" stroke-width="2.5"/></svg></span></div>
  <p class="step-copy">Lorem ipsum dolor sit amet, co nsetg hcletur adipiscing elit, sed do eiusmod tempor incididunt ut labore et dolore magna aliqua. Ut enim ad minim veniam, quis nostrud exercitation ullamco laboris nisi ut aliquip ex ea commodo consequat. Duis aute irure dolor</p>
  <div class="process-window" role="img" aria-label="Black framed square window with frosted glass"><span></span></div>
</section>

<footer class="site-footer">
  <div class="footer-brand"><span class="brand-dot"></span><span class="brand-name">Corvenhall Aluminium Windows &amp; Doors</span></div>
  <div class="footer-col" style="left:388px">
    <h4>Location</h4>
    <p>42 Kestrel Lane,<br>Sydney, NSW 2010 AU</p>
  </div>
  <div class="footer-col" style="left:624px">
    <h4>Contact Us</h4>
    <p class="contact-line"><svg width="16" height="16" viewBox="0 0 16 16"><path d="M3 1h3l1.5 4-2 1.2a9 9 0 004.3 4.3l1.2-2 4 1.5v3c0 1-1 2-2 2C7 15 1 9 1 3c0-1 1-2 2-2z" fill="#fff"/></svg>+61 2 5550 0148</p>
    <p class="contact-line"><svg width="16" height="16" viewBox="0 0 16 16"><rect x="1" y="3" width="14" height="10" rx="1" fill="#fff"/><path d="M1 4l7 5 7-5" stroke="#1e88f0" stroke-width="1.5" fill="none"/></svg>info@corvenhall.example</p>
  </div>
  <div class="footer-col" style="left:912px">
    <h4>Quality Assurance</h4>
    <div class="badge" role="img" aria-label="Quality certification badge"></div>
  </div>
</footer>
<div class="footer-bar">
  <span class="copy">Copyright &copy; 2023 All rights reserved</span>
  <span class="links"><span>Our Products</span><span>|</span><span>Why Corvenhall</span><span>|</span><span>Make an Enquiry</span><span>|</span><span>Our Blog</span></span>
</div>

</body>
</html>
```